Business Cards

Need a neat design for a new business card

Industry/Entity Type

Residential Construction

Contact Information for Business Card

Company Name- KOVE Construction Inc.
Owner- Marcus Tolliver
Phone number- (555)203-7481
Email- kovecohomes@brindlemail.example
Facebook- www.socialpage.example/kovecohomes

Colors
fefdec

```html
<!DOCTYPE html>
<html lang="en">
<head>
<meta charset="utf-8">
<title>KOVE Construction Inc. — Business Card</title>
<link rel="stylesheet" href="https://fonts.googleapis.com/css2?family=Cinzel:wght@400;500&family=Montserrat:wght@400;500&display=swap">
<style>
  :root {
    --stage: #262626;
    --card: #0b0b0b;
    --ink: #fefdec;
    --silver: #c9c9c4;
    --pattern-a: #141414;
    --pattern-b: #1c1c1c;
  }
  * { box-sizing: border-box; margin: 0; padding: 0; }
  html, body { width: 1200px; height: 900px; overflow: hidden; }
  body {
    background: var(--stage);
    display: flex;
    flex-direction: column;
    align-items: center;
    justify-content: center;
    gap: 30px;
    font-family: "Montserrat", sans-serif;
    color: var(--ink);
  }
  .card {
    position: relative;
    width: 700px;
    height: 400px;
    background: var(--card);
    overflow: hidden;
  }
  /* Front */
  .card-front__pattern {
    position: absolute; inset: 0;
    background: radial-gradient(ellipse at center, var(--pattern-b), var(--pattern-a) 75%);
  }
  .card-front__brand {
    position: absolute; inset: 0;
    display: flex; flex-direction: column;
    align-items: center; justify-content: center;
  }
  .brand-name--large {
    font-family: "Cinzel", serif;
    font-weight: 400;
    font-size: 84px;
    letter-spacing: 10px;
    color: var(--silver);
    line-height: 1;
  }
  .brand-tag--large {
    font-family: "Montserrat", sans-serif;
    font-weight: 500;
    font-size: 20px;
    letter-spacing: 7px;
    color: var(--silver);
    margin-top: 14px;
  }
  /* Back */
  .holder {
    position: absolute; left: 48px; top: 62px;
    font-family: "Cinzel", serif;
  }
  .holder__name { font-size: 26px; letter-spacing: 1px; }
  .holder__role { font-size: 13px; letter-spacing: 1px; margin-top: -2px; }
  .brand-lockup {
    position: absolute; right: 40px; top: 118px;
    display: flex; align-items: center; gap: 18px;
  }
  .brand-lockup__mark {
    font-family: "Cinzel", serif;
    font-size: 32px;
    display: flex; align-items: center; gap: 8px;
  }
  .brand-lockup__square { width: 12px; height: 12px; background: var(--ink); }
  .brand-lockup__divider { width: 1px; height: 82px; background: var(--ink); }
  .brand-lockup__text { display: flex; flex-direction: column; }
  .brand-lockup__name { font-family: "Cinzel", serif; font-size: 46px; letter-spacing: 3px; line-height: 1; }
  .brand-lockup__tag { font-size: 13px; letter-spacing: 4px; margin-top: 6px; }
  .contacts {
    position: absolute; left: 350px; top: 256px;
    font-size: 15px; letter-spacing: 0.3px; line-height: 24px;
  }
  .contacts__row { display: flex; align-items: center; gap: 10px; white-space: nowrap; }
  .contacts__row svg { width: 16px; height: 16px; flex: none; }
  .contacts__rule { width: 18px; height: 1px; background: var(--ink); margin: 30px 0 0 0; }
  .social {
    position: absolute; left: 332px; top: 350px;
    display: flex; align-items: center; gap: 12px;
    font-size: 16px; letter-spacing: 0.3px; white-space: nowrap;
  }
  .social__dot { width: 18px; height: 18px; border-radius: 50%; background: var(--ink); flex: none; }
</style>
</head>
<body>
  <section class="card card-front" aria-label="Card front">
    <div class="card-front__pattern" role="img" aria-label="Faint repeated decorative pattern across the card"></div>
    <div class="card-front__brand">
      <div class="brand-name--large">KOVE</div>
      <div class="brand-tag--large">CONSTRUCTION</div>
    </div>
  </section>

  <section class="card card-back" aria-label="Card back">
    <div class="holder">
      <div class="holder__name">MARCUS TOLLIVER</div>
      <div class="holder__role">Owner</div>
    </div>

    <div class="brand-lockup">
      <div class="brand-lockup__mark"><span class="brand-lockup__square"></span>KOVE</div>
      <div class="brand-lockup__divider"></div>
      <div class="brand-lockup__text">
        <span class="brand-lockup__name">KOVE</span>
        <span class="brand-lockup__tag">CONSTRUCTION</span>
      </div>
    </div>

    <div class="contacts">
      <div class="contacts__row">
        <svg viewBox="0 0 16 16" fill="none" stroke="currentColor" stroke-width="1.3">
          <circle cx="8" cy="8" r="7"/>
          <path d="M5.5 4.5l1.3 1.4-.7 1.1c.5 1 1.3 1.8 2.3 2.3l1.1-.7 1.4 1.3-.8 1c-2.6-.3-4.8-2.5-5.1-5.1z"/>
        </svg>
        <span>(555) 203-7481</span>
      </div>
      <div class="contacts__row">
        <svg viewBox="0 0 16 16" fill="none" stroke="currentColor" stroke-width="1.3">
          <rect x="1.5" y="3.5" width="13" height="9"/>
          <path d="M1.5 3.5L8 9l6.5-5.5"/>
        </svg>
        <span>kovecohomes@brindlemail.example</span>
      </div>
      <div class="contacts__rule"></div>
    </div>

    <div class="social">
      <span class="social__dot"></span>
      <span>socialpage.example/kovecohomes</span>
    </div>
  </section>
</body>
</html>
```